PixelGuild CEO Needs a Graphic for a Blog About Crowdsourcing and Online Employment

We need a simple graphic / banner for a blog post that's going to be posted on a large publication (like ByteHerald, Marlowe Commerce Quarterly).

The article will be written by Bram Ostiver (PixelGuild's CEO) and the title will be "Why Websites Will Become the Biggest Employers in the World". The article is about why online employers (like PixelGuild and Tasklynx) will one day have more 'workers' than offline employers.

We'd really like to get this ASAP - so early submissions encouraged. We will try and get the winning designer linked to from the article.

Note that this brief is similar to a previous project that we ran http://jobs.pixelguild-example.com/job.aspx?id=58213 where the article and design was published on ByteHerald http://byteherald-example.com/2012/12/08/asias-hidden-gig-surge/ and the designer (Moravia) was linked to from ByteHerald.

Target Market(s)

Entrepreneurs, journalists, small business owners, tech people.

Industry/Entity Type

Business

Requirements
Must have
• The graphic SHOULD have:
1) Have the text "Why Websites Will Become the Biggest Employers in the World" with some nice design and fonts (consider grey subtle pattern background and white drop shadow on fonts) - see attached examples
2) Have the dimensions 640px wide by 240px wide
Nice to have
• The graphic COULD have:

1) Incorporate the following words in the background (like a word cloud): crowdsource, microtask, crowdfund, witkey, outsource, freelance, online, work from home

OR

2) Incorporate logos of new online employers (Tasklynx, vYard, PixelGuild, ChoreFinch, Lunqiaofu, ClockworkPawn, Frameharbor) into the design. If the background of the graphic is grey, ideally, these logos would also be greyscale i.e. they should form a background motif.

OR

3) Show some graphic communicating themes from the article e.g. laptop, globe, workers, connections across the globe

OR

4) Have a second line of text "Why Crowdsourcing Websites Will Overtake Traditional Employers"
Should not have
• Should NOT have:
1) Any photos or clipart

```html
<!DOCTYPE html>
<html lang="en">
<head>
<meta charset="utf-8">
<title>Why Websites Will Become the Biggest Employers in the World</title>
<link rel="stylesheet" href="https://fonts.googleapis.com/css2?family=Arimo:wght@400&family=Nunito+Sans:wght@800&display=swap">
<style>
  :root {
    --bg-centre: #f2f2f2;
    --bg-mid: #b9b9b9;
    --bg-edge: #626262;
    --cloud-word: #ffffff;
    --cloud-faint: rgba(255, 255, 255, 0.55);
    --title-ink: #4b4b4b;
    --title-glow: #ffffff;
  }
  html, body {
    margin: 0;
    padding: 0;
    width: 1200px;
    height: 450px;
    overflow: hidden;
    background: var(--bg-edge);
  }
  .banner {
    display: block;
    width: 1200px;
    height: 450px;
  }
  .cloud-word {
    font-family: "Arimo", Arial, sans-serif;
    font-weight: 400;
    fill: var(--cloud-word);
  }
  .cloud-word--faint {
    fill: var(--cloud-faint);
  }
  .headline {
    font-family: "Nunito Sans", "Arial Black", sans-serif;
    font-weight: 800;
    font-size: 58px;
    fill: var(--title-ink);
  }
</style>
</head>
<body>
<svg class="banner" viewBox="0 0 1200 450" xmlns="http://www.w3.org/2000/svg">
  <defs>
    <radialGradient id="banner-backdrop" cx="50%" cy="48%" r="70%" fx="50%" fy="48%">
      <stop offset="0" stop-color="var(--bg-centre)"/>
      <stop offset="0.45" stop-color="var(--bg-mid)"/>
      <stop offset="1" stop-color="var(--bg-edge)"/>
    </radialGradient>
    <filter id="headline-glow" x="-5%" y="-30%" width="110%" height="160%">
      <feGaussianBlur in="SourceAlpha" stdDeviation="3" result="spread"/>
      <feFlood flood-color="#ffffff" flood-opacity="0.95"/>
      <feComposite in2="spread" operator="in" result="glow"/>
      <feGaussianBlur in="SourceGraphic" stdDeviation="1.1" result="soft"/>
      <feMerge>
        <feMergeNode in="glow"/>
        <feMergeNode in="glow"/>
        <feMergeNode in="soft"/>
      </feMerge>
    </filter>
  </defs>

  <rect class="backdrop" width="1200" height="450" fill="url(#banner-backdrop)"/>

  <g class="word-cloud">
    <text class="cloud-word" x="34" y="58" font-size="19">online</text>
    <text class="cloud-word" x="643" y="72" font-size="58">witkey</text>
    <text class="cloud-word" x="319" y="128" font-size="32">crowdsource</text>
    <text class="cloud-word cloud-word--faint" x="520" y="165" font-size="24">outsource</text>
    <text class="cloud-word" x="381" y="302" font-size="24">work from home</text>
    <text class="cloud-word" x="943" y="300" font-size="32">freelance</text>
    <text class="cloud-word" x="79" y="370" font-size="38">crowdfund</text>
    <text class="cloud-word" x="548" y="372" font-size="58">microtask</text>
  </g>

  <g class="headline-group" filter="url(#headline-glow)">
    <text class="headline" x="15" y="196" textLength="1170" lengthAdjust="spacingAndGlyphs">Why Websites Will Become the Biggest</text>
    <text class="headline" x="244" y="264" textLength="712" lengthAdjust="spacingAndGlyphs">Employers in the World</text>
  </g>
</svg>
</body>
</html>
```